Invest in Real Estate housing and apartment development projects in Lima - Peru

Need a presentation for Grupo Velmira, a top Real Estate developer from Peru who is looking for new leading investors such as Top Regional and Worldwide Real Estate funds and Regional Family offices and High Networth individuals to invest in Real Estate projects developed by/with Grupo Velmira. Velmira is focused on middle income apartments (housing) and has developed and delivered aprox 1400 apartments, and is currently developing and building 400 apartments. Velmira currently has a potential to develop 1500 more apartments. And is looking to raise between US $50 and 60mm dollars a year in additional new investments, all focused on real estate housing (essentially vertical housing, apartments)
I have already some information and slides prepared with information regarding management fees, development and sales/marketing fees, success fees which are alligned to IRR of the project.

Target Market(s)

Real Estate investors in Latin America

Industry/Entity Type

Real Estate Development

Colors

Designer to choose colors to be used in the design.

Requirements
Must have
• Graphs and pictures of real estate projects. Data of housing market from Lima, capital of Peru compared to other top capitals in South America

```html
<!DOCTYPE html>
<html lang="es">
<head>
<meta charset="utf-8">
<title>Grupo Velmira – Presentación a inversionistas</title>
<link rel="stylesheet" href="https://fonts.googleapis.com/css2?family=Lato:wght@300;400;700&display=swap">
<style>
  :root{
    --bg:#ea7a1e;
    --green:#73b43f;
    --green-dark:#5f9e30;
    --green-light:#c9dc3a;
    --yellow:#f6e01a;
    --ink:#4a4a4a;
    --muted:#8a8a8a;
    --grid:#e2e2e2;
    --white:#ffffff;
  }
  *{box-sizing:border-box;margin:0;padding:0}
  html,body{width:1200px;height:900px;overflow:hidden;background:var(--bg)}
  body{font-family:'Lato',sans-serif;color:var(--ink)}
  .stage{position:relative;width:1200px;height:900px;overflow:hidden}
  .slide{position:absolute;width:366px;height:275px;background:var(--white)}
  .frame{position:absolute;inset:7px;border:1.5px solid var(--green);pointer-events:none}
  .page-num{position:absolute;left:334px;top:246px;width:17px;height:17px;border-radius:50%;
    background:var(--green);color:var(--white);font-size:10px;line-height:17px;text-align:center}
  .slide-title{position:absolute;left:0;right:0;text-align:center;color:var(--green);font-weight:400;font-size:17px;line-height:21px}
  .photo{background:linear-gradient(160deg,#b9c9b0,#7c8f6e 55%,#c9b79a)}
  .avatar{border-radius:50%;border:1.5px solid var(--green);background:linear-gradient(180deg,#c8b8a8,#6e625a)}

  /* slide 6 – chart */
  .s-market{left:26px;top:146px}
  .s-market .slide-title{top:16px}
  .chart{position:absolute;left:0;top:0}

  /* slide 7 – track record */
  .s-track{left:426px;top:146px}
  .s-track .slide-title{top:19px}
  .s-track .subtitle{position:absolute;top:39px;left:0;right:0;text-align:center;font-size:8.5px;color:var(--ink);font-weight:300}
  .project{position:absolute;top:62px;width:106px}
  .project .photo{height:96px}
  .project-body{margin:0 8px 0 8px;border-left:1px solid var(--green);border-right:1px solid var(--green);border-bottom:1px solid var(--green);height:94px;position:relative;padding:0 4px}
  .project-name{font-size:13px;color:var(--green);font-weight:400;line-height:15px;padding-top:2px}
  .project-text{font-size:4px;line-height:5.6px;color:var(--ink);padding-top:2px}
  .project-text.en{margin-top:3px;padding-top:3px;border-top:1px solid var(--green-light)}
  .delivered{position:absolute;left:0;bottom:0;background:var(--green);color:var(--white);font-size:4.5px;padding:1px 4px;letter-spacing:.2px}

  /* slide 8 – directors */
  .s-board{left:818px;top:146px}
  .s-board .slide-title{top:19px}
  .brand{position:absolute;display:flex;align-items:center;gap:5px;color:var(--ink);font-weight:700;letter-spacing:.5px}
  .brand-dot{border-radius:50%;background:var(--green)}
  .s-board .brand{left:0;right:0;justify-content:center;top:50px;font-size:15px}
  .s-board .brand-dot{width:18px;height:18px}
  .connector{position:absolute;width:1px;background:var(--green)}
  .director{position:absolute;top:118px;width:80px;height:86px;background:var(--green);color:var(--white);text-align:center;padding:12px 5px 0}
  .director .avatar{position:absolute;left:22px;top:-29px;width:36px;height:36px;border:2px solid var(--white)}
  .director-name{font-size:6.5px;font-weight:700;line-height:8px}
  .director-role{font-size:4.5px;line-height:5.5px;min-height:11px}
  .director-list{list-style:none;text-align:left;margin-top:4px;border-top:1px solid rgba(255,255,255,.6);padding-top:4px}
  .director-list li{font-size:3.4px;line-height:4.2px;position:relative;padding-left:5px;margin-bottom:3px}
  .director-list li::before{content:"";position:absolute;left:0;top:.5px;width:3px;height:3px;border-radius:50%;background:var(--white)}

  /* slide 9 – agents */
  .s-agents{left:213px;top:478px}
  .s-agents .section-title{position:absolute;left:18px;top:22px;font-size:14px;color:var(--green);font-weight:400;padding-bottom:3px;border-bottom:1px solid var(--green);width:152px;white-space:nowrap}
  .s-agents .section-sub{position:absolute;left:18px;top:44px;font-size:6px;color:var(--ink)}
  .rule{position:absolute;height:1px;background:var(--green)}
  .agent{position:absolute;width:70px;text-align:center}
  .agent .avatar{width:56px;height:56px;margin:0 auto}
  .agent-name{font-size:5px;color:var(--green);margin-top:4px;line-height:6px}
  .agent-role{font-size:4px;font-weight:700;color:var(--ink);line-height:5px}
  .socials{display:flex;justify-content:center;gap:3px;margin-top:4px}
  .socials span{width:10px;height:10px;border-radius:50%;background:#b7b7b7}

  /* slide 10 – closing */
  .s-thanks{left:606px;top:478px}
  .s-thanks .photo{position:absolute;left:7px;top:30px;width:352px;height:74px;background:linear-gradient(180deg,#7e9a6c,#b59a76 60%,#8c7a62)}
  .thanks{position:absolute;top:107px;left:0;right:0;text-align:center;font-size:30px;color:var(--green);font-weight:400;letter-spacing:.5px}
  .s-thanks .divider{left:105px;top:160px;width:153px}
  .s-thanks .brand{left:0;right:0;justify-content:center;top:175px;font-size:17px}
  .s-thanks .brand-dot{width:20px;height:20px}
  .contact{position:absolute;top:208px;left:0;right:0;text-align:center;font-size:6px;line-height:7.5px;color:var(--ink)}
  .s-thanks .socials{position:absolute;left:0;right:0;top:240px;gap:6px}
  .s-thanks .socials span{width:14px;height:14px;background:var(--green)}
</style>
</head>
<body>
<main class="stage">

  <!-- 6: market opportunity -->
  <section class="slide s-market">
    <div class="frame"></div>
    <h2 class="slide-title">Por qué invertir en real estate<br>supone una oportunidad</h2>
    <svg class="chart" width="366" height="275" viewBox="0 0 366 275" aria-label="Gráfico de barras de oportunidad de inversión">
      <g stroke="var(--grid)" stroke-width="1">
        <line x1="77" y1="70" x2="77" y2="224"/><line x1="106" y1="70" x2="106" y2="224"/>
        <line x1="135" y1="70" x2="135" y2="224"/><line x1="164" y1="70" x2="164" y2="224"/>
        <line x1="194" y1="70" x2="194" y2="224"/><line x1="223" y1="70" x2="223" y2="224"/>
        <line x1="252" y1="70" x2="252" y2="224"/><line x1="281" y1="70" x2="281" y2="224"/>
      </g>
      <line x1="48" y1="68" x2="48" y2="226" stroke="#c9c9c9"/>
      <g>
        <rect x="48" y="88" width="29" height="15" fill="var(--yellow)"/><rect x="77" y="88" width="29" height="15" fill="var(--green-light)"/><rect x="106" y="88" width="58" height="15" fill="var(--green)"/>
        <rect x="48" y="113" width="88" height="15" fill="var(--yellow)"/><rect x="136" y="113" width="58" height="15" fill="var(--green-light)"/><rect x="194" y="113" width="87" height="15" fill="var(--green)"/>
        <rect x="48" y="139" width="117" height="15" fill="var(--yellow)"/><rect x="165" y="139" width="58" height="15" fill="var(--green-light)"/><rect x="223" y="139" width="29" height="15" fill="var(--green)"/>
        <rect x="48" y="165" width="29" height="15" fill="var(--yellow)"/><rect x="77" y="165" width="117" height="15" fill="var(--green-light)"/><rect x="194" y="165" width="87" height="15" fill="var(--green)"/>
        <rect x="48" y="190" width="58" height="15" fill="var(--yellow)"/><rect x="106" y="190" width="88" height="15" fill="var(--green-light)"/><rect x="194" y="190" width="58" height="15" fill="var(--green)"/>
      </g>
      <g font-family="Lato, sans-serif" font-size="9" text-anchor="middle">
        <circle cx="257" cy="120.5" r="12" fill="#fff" stroke="var(--green)" stroke-width="1.5"/><text x="257" y="124" fill="var(--green)">80</text>
        <circle cx="105" cy="146.5" r="12" fill="#fff" stroke="var(--green-light)" stroke-width="1.5"/><text x="105" y="150" fill="#b9b04a">20</text>
        <circle cx="148" cy="197.5" r="12" fill="#fff" stroke="var(--green-light)" stroke-width="1.5"/><text x="148" y="201" fill="#b9b04a">60</text>
      </g>
      <g font-family="Lato, sans-serif" font-size="7" fill="var(--muted)" text-anchor="middle">
        <text x="77" y="235">10</text><text x="106" y="235">20</text><text x="135" y="235">30</text><text x="164" y="235">40</text>
        <text x="194" y="235">50</text><text x="223" y="235">60</text><text x="252" y="235">70</text><text x="281" y="235">80</text>
      </g>
    </svg>
    <div class="page-num">6</div>
  </section>

  <!-- 7: track record -->
  <section class="slide s-track">
    <div class="frame"></div>
    <h2 class="slide-title">Velmira Edificaciones Track Record (1/2)</h2>
    <p class="subtitle">Proyectos ejecutados con resultados consistentes</p>

    <article class="project" style="left:16px">
      <div class="photo" role="img" aria-label="Render del proyecto Altavista con parque y ciclista"></div>
      <div class="project-body">
        <h3 class="project-name">ALTAVISTA</h3>
        <p class="project-text">Proyecto residencial de diseño innovador que satisface las exigencias de un estilo de vida moderno y funcional.</p>
        <p class="project-text en">An exclusive residential project with innovative design that meets the demands of a modern lifestyle.</p>
        <span class="delivered">DELIVERED 2015</span>
      </div>
    </article>

    <article class="project" style="left:130px">
      <div class="photo" role="img" aria-label="Render del proyecto Jacarandá con juegos infantiles entre edificios"></div>
      <div class="project-body">
        <h3 class="project-name">JACARANDÁ</h3>
        <p class="project-text">Proyecto residencial de diseño innovador que satisface las exigencias de un estilo de vida moderno y funcional.</p>
        <p class="project-text en">An exclusive residential project with innovative design that meets the demands of a modern lifestyle.</p>
        <span class="delivered">DELIVERED 2014</span>
      </div>
    </article>

    <article class="project" style="left:244px">
      <div class="photo" role="img" aria-label="Render del proyecto Los Laureles con edificio blanco y área de juegos"></div>
      <div class="project-body">
        <h3 class="project-name">LOS LAURELES</h3>
        <p class="project-text">Proyecto residencial de diseño innovador que satisface las exigencias de un estilo de vida moderno y funcional.</p>
        <p class="project-text en">An exclusive residential project with innovative design that meets the demands of a modern lifestyle.</p>
        <span class="delivered">DELIVERED 2017</span>
      </div>
    </article>
    <div class="page-num">7</div>
  </section>

  <!-- 8: directors -->
  <section class="slide s-board">
    <div class="frame"></div>
    <h2 class="slide-title">Nuestros Directores</h2>
    <div class="brand"><span class="brand-dot"></span>GRUPO VELMIRA</div>

    <span class="connector" style="left:57px;top:204px;height:64px"></span>
    <span class="connector" style="left:143px;top:204px;height:64px"></span>
    <span class="connector" style="left:228px;top:204px;height:64px"></span>
    <span class="connector" style="left:314px;top:204px;height:40px"></span>

    <article class="director" style="left:17px">
      <div class="avatar" role="img" aria-label="Retrato de Ricardo Almenara"></div>
      <h3 class="director-name">Ricardo Almenara</h3>
      <p class="director-role">Director, Comité de Operaciones</p>
      <ul class="director-list"><li>Ejecutivo senior con experiencia inmobiliaria</li><li>Real Estate Management</li><li>Master in Engineering of Design</li></ul>
    </article>
    <article class="director" style="left:103px">
      <div class="avatar" role="img" aria-label="Retrato de Tomás Quiroga"></div>
      <h3 class="director-name">Tomás Quiroga</h3>
      <p class="director-role">Presidente del Directorio, Comité de Nuevos Proyectos</p>
      <ul class="director-list"><li>Ejecutivo senior con experiencia inmobiliaria</li><li>Real Estate Management</li><li>Master in Engineering of Design</li></ul>
    </article>
    <article class="director" style="left:188px">
      <div class="avatar" role="img" aria-label="Retrato de Andrés Villacorta"></div>
      <h3 class="director-name">Andrés Villacorta</h3>
      <p class="director-role">Director, Comité de Inversiones</p>
      <ul class="director-list"><li>Ejecutivo senior con experiencia inmobiliaria</li><li>Real Estate Management</li><li>Master in Engineering of Design</li></ul>
    </article>
    <article class="director" style="left:274px">
      <div class="avatar" role="img" aria-label="Retrato de Luis Felipe Ocampo"></div>
      <h3 class="director-name">Luis Felipe Ocampo</h3>
      <p class="director-role">Director, Comité de Finanzas</p>
      <ul class="director-list"><li>Ejecutivo senior con experiencia inmobiliaria</li><li>Real Estate Management</li><li>Master in Engineering of Design</li></ul>
    </article>
    <div class="page-num">8</div>
  </section>

  <!-- 9: agents -->
  <section class="slide s-agents">
    <div class="frame"></div>
    <h2 class="section-title">ENCUENTRE A NUESTRO AGENTE</h2>
    <p class="section-sub">MEET OUR AGENT</p>
    <span class="rule" style="left:308px;top:90px;width:50px"></span>
    <span class="rule" style="left:8px;top:188px;width:44px"></span>

    <div class="agent" style="left:45px;top:62px"><div class="avatar" role="img" aria-label="Retrato de agente"></div><p class="agent-name">JOHN DOE</p><p class="agent-role">Realestate Champ</p><div class="socials"><span></span><span></span><span></span><span></span></div></div>
    <div class="agent" style="left:111px;top:62px"><div class="avatar" role="img" aria-label="Retrato de agente"></div><p class="agent-name">JANE DOE</p><p class="agent-role">Realestate Champ</p><div class="socials"><span></span><span></span><span></span><span></span></div></div>
    <div class="agent" style="left:178px;top:62px"><div class="avatar" role="img" aria-label="Retrato de agente"></div><p class="agent-name">JANE DOE</p><p class="agent-role">Realestate Champ</p><div class="socials"><span></span><span></span><span></span><span></span></div></div>
    <div class="agent" style="left:245px;top:62px"><div class="avatar" role="img" aria-label="Retrato de agente"></div><p class="agent-name">JOHN DOE</p><p class="agent-role">Realestate Champ</p><div class="socials"><span></span><span></span><span></span><span></span></div></div>

    <div class="agent" style="left:45px;top:160px"><div class="avatar" role="img" aria-label="Retrato de agente"></div><p class="agent-name">JOHN DOE</p><p class="agent-role">Realestate Champ</p><div class="socials"><span></span><span></span><span></span><span></span></div></div>
    <div class="agent" style="left:111px;top:160px"><div class="avatar" role="img" aria-label="Retrato de agente"></div><p class="agent-name">JANE DOE</p><p class="agent-role">Realestate Champ</p><div class="socials"><span></span><span></span><span></span><span></span></div></div>
    <div class="agent" style="left:178px;top:160px"><div class="avatar" role="img" aria-label="Retrato de agente"></div><p class="agent-name">JANE DOE</p><p class="agent-role">Realestate Champ</p><div class="socials"><span></span><span></span><span></span><span></span></div></div>
    <div class="agent" style="left:245px;top:160px"><div class="avatar" role="img" aria-label="Retrato de agente"></div><p class="agent-name">JOHN DOE</p><p class="agent-role">Realestate Champ</p><div class="socials"><span></span><span></span><span></span><span></span></div></div>
    <div class="page-num" style="top:256px">9</div>
  </section>

  <!-- 10: closing -->
  <section class="slide s-thanks">
    <div class="frame"></div>
    <div class="photo" role="img" aria-label="Terraza con pérgola de madera, mobiliario y muro verde"></div>
    <h2 class="thanks">GRACIAS</h2>
    <span class="rule divider"></span>
    <div class="brand"><span class="brand-dot"></span>GRUPO VELMIRA</div>
    <p class="contact">www.grupovelmira.example<br>Telephone Central: 400 1200 | contacto@grupovelmira.example<br>Grupo Velmira © 2016 - All rights reserved</p>
    <div class="socials"><span></span><span></span></div>
  </section>

</main>
</body>
</html>
```